We need a new e-commerce website. Designed and fully functional.

We are looking for someone who can re-create our website from A-Z and it is fully functional (turnkey). Currently we have a website that we do not like because it is too dark and not easy to use. We would like a more modern, minimalist, elegant, bright and very easy to use. We are also looking for a person who would agree to accompany us in the catalog (with payment in addition to race). To be defined later. We are a designer company, sold through the online store. The jewels are long necklaces with thematic pendants associated with semi-precious stones. 6 themes of pendants, 2 colors and 6 types of semi-precious stones that are combined according to desires. 72 possibilities of combinations. We already have all the connections, texts, payment possibilities, pictures that we all put at your disposal. You can have a look on our website on velmorik.com. We also have a little guide (attached) of what we are looking for this new website. The site must be in 2 languages (French-English) and 3 currencies (dollar, euro and Swiss francs). The shipping costs must be displayed according to the country of destination (KDX) in the shopping cart and for Switzerland the VAT must be displayed directly too. Name of the website: trévi manu jewelry (www.velmorik.com) E-Mail address for the website: info@velmorik.com This website must contain: Home: home page. Welcome page Shop: All articles About: About the creator Contact: e-mail and company contact Press: all the publications in the magazines FAQ & HELP: the company information, orders ... Account: the clients can create an account if they want Purchasing Pannier Languages: English-French Currencies: Dollar, Euro, Swiss Francs

Industry/Entity Type

Jewelry Store

Coding

Coded - Design and coding required

Font styles to use
Sans Serif

Colors

Designer to choose colors to be used in the design.

Requirements
Must have
• This website must be easy to use, modern, elegant and sober.

```html
<!DOCTYPE html>
<html lang="en">
<head>
<meta charset="utf-8">
<title>Trévi Manu Jewelry</title>
<link rel="stylesheet" href="https://fonts.googleapis.com/css2?family=Raleway:wght@200;400;500;700&display=swap">
<style>
  :root {
    --ink: #1a1a1a;
    --nav: #a3a3a3;
    --white: #ffffff;
    --band: #f1f1f1;
    --muted: #9a9a9a;
    --badge-red: #e3232c;
    --hero-rose: #dcbab3;
    --hero-gold: #d8ab66;
  }
  * { box-sizing: border-box; margin: 0; padding: 0; }
  html, body {
    width: 1200px; height: 1200px; overflow: hidden;
    background: var(--white);
    font-family: "Raleway", sans-serif;
    color: var(--ink);
  }
  .page { position: relative; width: 1200px; height: 1200px; }

  .site-header { position: absolute; top: 0; left: 0; width: 1200px; height: 240px; }
  .brand {
    position: absolute; left: 48px; top: 52px; width: 170px;
    display: flex; flex-direction: column; align-items: center; gap: 10px;
  }
  .brand-mark {
    width: 30px; height: 30px; border-radius: 50%;
    border: 1.5px solid var(--ink);
  }
  .brand-name {
    font-weight: 400; font-size: 17px; letter-spacing: 1.5px;
    color: var(--ink); text-align: center; line-height: 1.3;
  }
  .main-nav {
    position: absolute; left: 302px; top: 95px;
    display: flex; gap: 17px;
  }
  .main-nav a {
    font-size: 19px; font-weight: 400; color: var(--nav);
    text-decoration: none; letter-spacing: 0.2px;
  }

  .hero {
    position: absolute; left: 0; top: 241px; width: 1200px; height: 554px;
    background: linear-gradient(100deg, var(--hero-rose) 0%, var(--hero-rose) 45%, var(--hero-gold) 100%);
  }
  .hero-title {
    position: absolute; left: 218px; top: 503px;
    font-size: 43px; font-weight: 200; color: var(--white);
    letter-spacing: 0.5px; line-height: 1;
  }

  .social {
    position: absolute; top: 884px; left: 0; width: 1200px;
    text-align: center;
  }
  .social-title { font-size: 14.5px; font-weight: 500; letter-spacing: -0.2px; }
  .social-list {
    display: flex; justify-content: center; gap: 30px;
    margin-top: 34px; list-style: none;
  }
  .social-list a {
    font-size: 16px; font-weight: 700; color: var(--ink); text-decoration: none;
  }
  .design-badge {
    position: absolute; left: 566px; top: 1008px;
    width: 50px; height: 50px; background: var(--badge-red);
  }

  .legal-band {
    position: absolute; left: 0; top: 1111px; width: 1200px; height: 51px;
    background: var(--band);
    display: flex; align-items: center; justify-content: center;
  }
  .legal-band a { font-size: 14px; font-weight: 500; color: #444; text-decoration: none; }
  .site-footer {
    position: absolute; left: 0; top: 1177px; width: 1200px;
    text-align: center; font-size: 13px; color: var(--muted);
  }
  .site-footer strong { font-weight: 500; color: #777; }
  .site-footer .updated { color: var(--ink); font-weight: 500; margin-left: 4px; }
</style>
</head>
<body>
<div class="page">
  <header class="site-header">
    <div class="brand">
      <span class="brand-mark"></span>
      <span class="brand-name">TRÉVI MANU JEWELRY</span>
    </div>
    <nav class="main-nav">
      <a href="#">Home</a>
      <a href="#">Shop</a>
      <a href="#">About</a>
      <a href="#">Contact</a>
      <a href="#">Press</a>
      <a href="#">FAQ</a>
      <a href="#">Account</a>
      <a href="#">Purchasing</a>
      <a href="#">Languages</a>
      <a href="#">Currencies</a>
    </nav>
  </header>

  <section class="hero" role="img" aria-label="Product photograph: gold pendant with a citrine drop on a long necklace of citrine beads, on a soft pink surface"></section>
  <h1 class="hero-title">ELEGANCE BY NATURE</h1>

  <section class="social">
    <h2 class="social-title">FOLLOW US ON SOCIAL MEDIA</h2>
    <ul class="social-list">
      <li><a href="#">Chirpa</a></li>
      <li><a href="#">Snapgrid</a></li>
      <li><a href="#">Tackly</a></li>
      <li><a href="#">Circlo</a></li>
    </ul>
  </section>
  <div class="design-badge" aria-label="Design label"></div>

  <div class="legal-band"><a href="#">Terms &amp; Conditions</a></div>
  <footer class="site-footer">
    Trévi Manu Jewelry © 2019 - Studio Lémanique <strong>joaillerie</strong> &amp; <strong>site internet Vaud</strong> -
    <span class="updated">Derniere mise a jour le 11.02.2019</span>
  </footer>
</div>
</body>
</html>
```